Freelance business trainer needs a new business card

My business is called Tbrite. I provide training in the workplace on management, coaching and mentoring, and customer service topics for a variety of businesses, colleges and private training providers, and teach on management programs. I need a professional but eye catching business card. Business colours grey and orange. My name Linda Marchbank; Tel 07853 416207; email lmarchbank@tbrite.co.uk; website www.tbrite.co.uk.
Happy to have some sort of logo on front and details on back or all on one side
Target Market(s)
SME businesses and colleges - workshops i run are for adults in the workplace
Industry/Entity Type
Training
Look and feel

```html
<!DOCTYPE html>
<html lang="en">
<head>
<meta charset="utf-8">
<title>Tbrite business card – front and back</title>
<link href="https://fonts.googleapis.com/css2?family=Lato:wght@400;700;900&display=swap" rel="stylesheet">
<style>
  :root {
    --charcoal: #333333;
    --orange: #f7901e;
    --white: #ffffff;
    --backdrop: #e9e6e2;
  }
  html, body {
    margin: 0;
    padding: 0;
    width: 1200px;
    height: 900px;
    overflow: hidden;
    background: var(--backdrop);
  }
  .canvas {
    width: 1200px;
    height: 900px;
    display: flex;
    flex-direction: column;
    align-items: center;
    justify-content: center;
    gap: 48px;
  }
  .card {
    display: block;
    width: 660px;
    height: 377px;
    filter: drop-shadow(0 6px 14px rgba(0,0,0,0.18));
  }
  .fill-charcoal { fill: var(--charcoal); }
  .fill-orange { fill: var(--orange); }
  .brand-name {
    font-family: "Lato", sans-serif;
    font-weight: 900;
    font-size: 64px;
    fill: var(--white);
    letter-spacing: 0.5px;
  }
  .holder-name {
    font-family: "Lato", sans-serif;
    font-weight: 700;
    font-size: 24px;
    fill: var(--orange);
  }
  .holder-role {
    font-family: "Lato", sans-serif;
    font-weight: 700;
    font-size: 16px;
    fill: var(--white);
  }
  .contact-line {
    font-family: "Lato", sans-serif;
    font-weight: 400;
    font-size: 15px;
    fill: var(--charcoal);
  }
  .icon-badge { fill: var(--orange); }
  .icon-glyph { fill: var(--charcoal); }
  .icon-stroke { fill: none; stroke: var(--charcoal); stroke-width: 1.6; stroke-linejoin: round; }
</style>
</head>
<body>
<main class="canvas">

  <!-- Card front: brand side -->
  <svg class="card card-front" viewBox="0 0 660 377" role="img" aria-label="Tbrite card front">
    <polygon class="fill-charcoal"
      points="0,0 660,0 660,118 632,128 646,142 624,150 660,170 660,377 0,377"/>
    <polygon class="fill-orange" points="0,0 300,0 365,377 0,377"/>
    <text class="brand-name" x="330" y="210" text-anchor="middle">Tbrite</text>
  </svg>

  <!-- Card back: contact side -->
  <svg class="card card-back" viewBox="0 0 660 377" role="img" aria-label="Tbrite card back with contact details">
    <polygon class="fill-charcoal"
      points="0,0 660,0 660,377 0,377 0,318 14,306 4,296 26,284 0,270"/>
    <polygon class="fill-orange"
      points="330,0 660,0 660,377 480,377 446,270 462,262 448,222 398,204 414,194 400,154 352,136 370,124"/>

    <g class="contact-icons">
      <g class="icon icon-phone" transform="translate(348,150)">
        <circle class="icon-badge" r="15"/>
        <path class="icon-glyph" d="M-6,-7 q-3,2 -1,7 q3,7 9,9 q4,1 6,-2 l-3,-3 q-2,1 -3,0 q-3,-2 -5,-5 q-1,-2 0,-3 z"/>
      </g>
      <g class="icon icon-telephone" transform="translate(394,212)">
        <circle class="icon-badge" r="15"/>
        <path class="icon-glyph" d="M-9,-3 q0,-5 9,-5 q9,0 9,5 l0,2 l-4,0 l0,-2 l-10,0 l0,2 l-4,0 z"/>
        <path class="icon-glyph" d="M-6,0 l12,0 l2,7 l-16,0 z"/>
        <circle r="2.2" cy="3.5" fill="var(--orange)"/>
      </g>
      <g class="icon icon-envelope" transform="translate(438,280)">
        <circle class="icon-badge" r="15"/>
        <rect class="icon-glyph" x="-8" y="-6" width="16" height="12" rx="1"/>
        <path d="M-8,-6 l8,6 l8,-6" fill="none" stroke="var(--orange)" stroke-width="1.4"/>
      </g>
    </g>

    <g class="contact-details">
      <text class="contact-line" x="392" y="116">07853 416207</text>
      <text class="contact-line" x="438" y="176">lmarchbank@tbrite.co.uk</text>
      <text class="contact-line" x="480" y="246">www.tbrite.co.uk</text>
    </g>

    <g class="card-holder">
      <text class="holder-name" x="150" y="292">Linda Marchbank</text>
      <text class="holder-role" x="150" y="314">Manager</text>
    </g>
  </svg>

</main>
</body>
</html>
```